Stationary and document suite for consultancy business in Australia called Torvessa

I would like to get a suite of documents suitable for my new business called Torvessa. I have included the original brief below, however have already selected a design for the logo. I would like to get:
Letter head - simple letter template with "V" logo embossed in background
Word document - standard format with "V" logo embossed in background
Proposal document - bolder pages with cover and back cover, include empty pages with footer as well as contents
Powerpoint presentation - open to ideas
Email signature - banner style or text, open to ideas
Brief that was given for logo (logo not required)
The name of the business is derived from the latin word for green ("Viridis") combined with "co" which is intended to represent a number of different words: collaborative, cooperative, coaching, collective,  construction, consulting, etc.
My objective for the brand is to represent a dynamic, progressive and collaborative business, where our people have fun and enjoy their work.
The objective of our business is to provide consultancy services to construction businesses, mainly aimed at building high performing teams and strategic growth. We will create learning and development tools that businesses can use to increase staff satisfaction and retention. Our future goal is to invest in decarbonisation and sustainability technology for use in the construction industry.
Our target market is construction business leaders and infrastructure owners, who operate road, rail and utility assets. We also want to present as a dynamic, progressive and fun place to work that will be attractive to new employees.

```html
<!DOCTYPE html>
<html lang="en">
<head>
<meta charset="utf-8">
<title>Torvessa — Letterhead</title>
<link href="https://fonts.googleapis.com/css2?family=Montserrat:wght@400;500&display=swap" rel="stylesheet">
<style>
  :root {
    --backdrop: #b9c2d2;
    --paper: #ffffff;
    --brand-grey: #7a7a7a;
    --brand-green: #8cc63f;
    --text-grey: #6f6f6f;
  }
  * { margin: 0; padding: 0; box-sizing: border-box; }
  html, body {
    width: 1200px;
    height: 900px;
    overflow: hidden;
    background: var(--backdrop);
    font-family: "Montserrat", sans-serif;
  }
  .canvas {
    width: 1200px;
    height: 900px;
    display: flex;
    align-items: center;
    justify-content: center;
  }
  .letterhead {
    position: relative;
    width: 594px;
    height: 840px;
    background: var(--paper);
    box-shadow: 0 8px 30px rgba(40, 50, 70, 0.25);
    overflow: hidden;
  }
  .brand {
    position: absolute;
    top: 64px;
    left: 50px;
    display: flex;
    align-items: center;
    gap: 9px;
  }
  .brand-dot {
    width: 12px;
    height: 12px;
    border-radius: 50%;
    background: var(--brand-green);
  }
  .brand-name {
    font-size: 32px;
    font-weight: 500;
    letter-spacing: 0.5px;
    line-height: 1;
    color: var(--brand-grey);
  }
  .contact {
    position: absolute;
    right: 34px;
    bottom: 26px;
    list-style: none;
    font-size: 9.5px;
    line-height: 16px;
    color: var(--text-grey);
  }
  .contact li {
    display: flex;
    align-items: center;
    gap: 8px;
    white-space: nowrap;
  }
  .contact svg {
    width: 9px;
    height: 9px;
    flex: none;
    fill: var(--brand-green);
  }
  .footer-rule {
    position: absolute;
    height: 4px;
  }
  .footer-rule--grey {
    left: 0;
    width: 430px;
    bottom: 14px;
    background: var(--brand-grey);
  }
  .footer-rule--green {
    right: 0;
    width: 164px;
    bottom: 0;
    background: var(--brand-green);
  }
</style>
</head>
<body>
<main class="canvas">
  <section class="letterhead">
    <header class="brand">
      <span class="brand-dot"></span>
      <span class="brand-name">Torvessa</span>
    </header>

    <ul class="contact">
      <li>
        <svg viewBox="0 0 10 10" aria-hidden="true"><path d="M2 0.5 L3.6 0.5 L4.3 2.8 L3.2 3.6 Q4.2 5.8 6.4 6.8 L7.2 5.7 L9.5 6.4 L9.5 8 Q9.5 9.5 8 9.5 Q0.5 9 0.5 2 Q0.5 0.5 2 0.5 Z"/></svg>
        <span>412 555 0196</span>
      </li>
      <li>
        <svg viewBox="0 0 10 10" aria-hidden="true"><path d="M0.5 2 H9.5 V8 H0.5 Z M0.5 2 L5 5.5 L9.5 2" fill="none" stroke="#8cc63f" stroke-width="1.2"/></svg>
        <span>info@torvessa.co</span>
      </li>
      <li>
        <svg viewBox="0 0 10 10" aria-hidden="true"><circle cx="5" cy="5" r="4.3" fill="none" stroke="#8cc63f" stroke-width="1.1"/><path d="M0.7 5 H9.3 M5 0.7 V9.3" stroke="#8cc63f" stroke-width="0.9"/></svg>
        <span>www.torvessa.co</span>
      </li>
    </ul>

    <div class="footer-rule footer-rule--grey"></div>
    <div class="footer-rule footer-rule--green"></div>
  </section>
</main>
</body>
</html>
```